My new Bible based podcast needs a Podcast Cover Design for Vexora directory

I need a Podcast Cover Design design for my podcast listing in Vexora. The podcast is called Morning Lanterns Over Hills. I would like something cheerful, warm, and fresh because I take a non-traditional approach to explaining how the Bible is relevant to people today. My goal is to get back to the original spirituality of the Bible without all the centuries of added man-made doctrines. It would be great to show a sense of peace and hope, with new possibilities. This is not like a floating corporate logo. I need it to be square and full color/design all the way to the edges.

I have resubmitted this project because I did not understand how to ask for a podcast cover design. If you already submitted for me, I apologize for not knowing how the system works. I did not give the best picture of what I needed.

Target Market(s)

People who want a fresh look at the Bible

Industry/Entity Type

Religious

Logo Text

Morning Lanterns Over Hills

Colors

Designer to choose colors to be used in the design.

Requirements
Must have
• It must be square. The design should fill the space. See screen shot below of podcast cover designs on the Christianity/Spirituality page of Vexora directory so you can see where the podcast cover design needs to fit in and stand out.
• The final design will need to be:
• 3,000 x 3,000 pixels (but readable at 150 x 150)
• 72 dpi
• .jpg or .png format
• rgb color space
Nice to have
• Perhaps an open book suggesting the Bible, but not necessary.
Should not have
• No microphones or airwaves.

```html
<!DOCTYPE html>
<html lang="en">
<head>
<meta charset="utf-8">
<title>Morning Lanterns Over Hills — Podcast Cover</title>
<link rel="stylesheet" href="https://fonts.googleapis.com/css2?family=Kaushan+Script&display=swap">
<style>
  :root {
    --ink-white: #ffffff;
    --deep-navy: #12306e;
    --royal-blue: #1f4fb8;
    --ocean-blue: #1d7fb5;
    --teal: #2fa6c4;
    --pale-sky: #8fd0e6;
    --dawn-gold: #f6c36a;
    --dawn-peach: #f29a6b;
  }
  html, body {
    margin: 0;
    padding: 0;
    width: 1200px;
    height: 1200px;
    overflow: hidden;
    background: var(--deep-navy);
  }
  .podcast-cover {
    position: relative;
    width: 1200px;
    height: 1200px;
    overflow: hidden;
  }
  .watercolor-wash {
    position: absolute;
    inset: 0;
    width: 1200px;
    height: 1200px;
  }
  .cover-title {
    position: absolute;
    inset: 0;
    margin: 0;
    display: flex;
    flex-direction: column;
    align-items: center;
    justify-content: center;
    font-family: "Kaushan Script", cursive;
    font-weight: 400;
    color: var(--ink-white);
    line-height: 0.98;
    text-align: center;
    transform: rotate(-7deg);
  }
  .cover-title span { display: block; white-space: nowrap; }
  .cover-title .line-morning { font-size: 180px; margin-left: 80px; }
  .cover-title .line-lanterns { font-size: 220px; }
  .cover-title .line-hills { font-size: 160px; margin-left: 120px; }
</style>
</head>
<body>
  <main class="podcast-cover">
    <svg class="watercolor-wash" viewBox="0 0 1200 1200" role="img"
         aria-label="Full-bleed blue and teal watercolor wash with a warm dawn glow">
      <defs>
        <radialGradient id="baseWash" cx="45%" cy="42%" r="75%">
          <stop offset="0%" stop-color="var(--royal-blue)"/>
          <stop offset="38%" stop-color="var(--deep-navy)"/>
          <stop offset="70%" stop-color="var(--ocean-blue)"/>
          <stop offset="100%" stop-color="var(--teal)"/>
        </radialGradient>
        <radialGradient id="dawnGlow" cx="72%" cy="88%" r="55%">
          <stop offset="0%" stop-color="var(--dawn-gold)" stop-opacity="0.85"/>
          <stop offset="45%" stop-color="var(--dawn-peach)" stop-opacity="0.35"/>
          <stop offset="100%" stop-color="var(--dawn-peach)" stop-opacity="0"/>
        </radialGradient>
        <radialGradient id="skyGlow" cx="30%" cy="12%" r="40%">
          <stop offset="0%" stop-color="var(--pale-sky)" stop-opacity="0.5"/>
          <stop offset="100%" stop-color="var(--pale-sky)" stop-opacity="0"/>
        </radialGradient>
      </defs>
      <rect width="1200" height="1200" fill="url(#baseWash)"/>
      <rect width="1200" height="1200" fill="url(#skyGlow)"/>
      <rect width="1200" height="1200" fill="url(#dawnGlow)"/>
    </svg>
    <h1 class="cover-title">
      <span class="line-morning">Morning</span>
      <span class="line-lanterns">Lanterns</span>
      <span class="line-hills">Over Hills</span>
    </h1>
  </main>
</body>
</html>
```